Name of business TRV Harbor Advisory Group, LP.
business focuses on hotel investments and real estate deals, on the bottom of the card I need my partner company listed as "Strategic Partner of Weld Lodging Group" www.weldlodginggroup.example and the logo that is attached for them on the bottom also

I am the Principal of the business

Industry/Entity Type

Real Estate

Contact Information for Business Card

Dorian Kells
582 Farrow Street
Lebanon, TN 37195
C- 615-302-4418
D- 615-719-2083
F- 615-866-3147

```html
<!DOCTYPE html>
<html lang="en">
<head>
<meta charset="utf-8">
<title>Dorian Kells – Business Card</title>
<link href="https://fonts.googleapis.com/css2?family=Lato:wght@400;700&display=swap" rel="stylesheet">
<style>
  :root {
    --backdrop: #e9e7e3;
    --card-white: #ffffff;
    --card-black: #1c1c1c;
    --brand-green: #3bb54a;
    --ink: #1a1a1a;
    --mark-grey: #7d7c7a;
    --contact-white: #f2f2f2;
    --muted-white: #bdbdbd;
  }
  * { margin: 0; padding: 0; box-sizing: border-box; }
  html, body {
    width: 1200px;
    height: 841px;
    overflow: hidden;
    background: var(--backdrop);
  }
  .canvas {
    width: 1200px;
    height: 841px;
    display: flex;
    align-items: center;
    justify-content: center;
  }
  .business-card {
    width: 980px;
    height: 560px;
    background: var(--card-black);
    box-shadow: 0 10px 30px rgba(0,0,0,0.18);
    font-family: "Lato", sans-serif;
    overflow: hidden;
    display: flex;
    flex-direction: column;
  }
  .card-header {
    height: 218px;
    flex: none;
    background: var(--card-white);
    border-bottom: 7px solid var(--brand-green);
    display: flex;
    align-items: center;
    padding-left: 120px;
    gap: 26px;
  }
  .monogram-disc {
    width: 96px;
    height: 96px;
    flex: none;
  }
  .name-block { display: flex; flex-direction: column; }
  .person-name {
    font-size: 64px;
    font-weight: 700;
    letter-spacing: -1px;
    line-height: 1.05;
    color: var(--ink);
  }
  .person-name .surname { color: var(--brand-green); }
  .person-title {
    font-size: 22px;
    font-weight: 400;
    letter-spacing: 3px;
    text-transform: uppercase;
    color: var(--mark-grey);
    margin-top: 4px;
  }
  .card-body {
    flex: 1;
    display: flex;
    flex-direction: column;
    padding: 34px 60px 26px 150px;
  }
  .company-name {
    font-size: 44px;
    font-weight: 400;
    line-height: 1.2;
    color: var(--brand-green);
    margin-bottom: 16px;
  }
  .contact-line {
    font-size: 25px;
    color: var(--contact-white);
    line-height: 1.45;
  }
  .contact-line + .contact-line { padding-left: 34px; }
  .contact-label {
    color: var(--brand-green);
    font-weight: 700;
  }
  .contact-item { margin-right: 12px; }
  .partner-strip {
    margin-top: auto;
    display: flex;
    align-items: center;
    justify-content: space-between;
    border-top: 1px solid #3a3a3a;
    padding-top: 16px;
  }
  .partner-text {
    font-size: 19px;
    line-height: 1.4;
    color: var(--contact-white);
  }
  .partner-web { color: var(--muted-white); }
  .partner-mark {
    display: flex;
    align-items: center;
    gap: 12px;
  }
  .partner-mark-square {
    width: 34px;
    height: 34px;
    flex: none;
  }
  .partner-mark-name {
    font-size: 22px;
    font-weight: 700;
    color: var(--contact-white);
  }
</style>
</head>
<body>
<main class="canvas">
  <article class="business-card">
    <header class="card-header">
      <svg class="monogram-disc" viewBox="0 0 96 96" aria-hidden="true">
        <circle cx="48" cy="48" r="48" fill="var(--mark-grey)"/>
      </svg>
      <div class="name-block">
        <h1 class="person-name">Dorian <span class="surname">Kells</span></h1>
        <p class="person-title">Principal</p>
      </div>
    </header>
    <section class="card-body">
      <p class="company-name">TRV Harbor Advisory Group, LP.</p>
      <p class="contact-line">
        <span class="contact-item"><span class="contact-label">Cell-</span> 615-302-4418</span>
        <span class="contact-item"><span class="contact-label">Land-</span> 615-719-2083</span>
        <span class="contact-item"><span class="contact-label">Fax-</span> 615-866-3147</span>
      </p>
      <p class="contact-line">
        <span class="contact-label">Address-</span> 582 Farrow Street Lebanon, TN 37195
      </p>
      <footer class="partner-strip">
        <div class="partner-text">
          <p>Strategic Partner of Weld Lodging Group</p>
          <p class="partner-web">www.weldlodginggroup.example</p>
        </div>
        <div class="partner-mark">
          <svg class="partner-mark-square" viewBox="0 0 34 34" aria-hidden="true">
            <rect width="34" height="34" fill="var(--brand-green)"/>
          </svg>
          <span class="partner-mark-name">Weld Lodging Group</span>
        </div>
      </footer>
    </section>
  </article>
</main>
</body>
</html>
```